Business card for wedding & event planning company

I'm looking for a well designed double sided business card to represent my wedding and event planning company.

It should include the fact we manage the following events:
Weddings, birthdays, conferences, product launches, fashion shows & conventions
in the following areas:
Wiltshire, Oxfordshire, Berkshire & London

My contact details to be included are:

Moira Pennock
07715 482036
moira@amberlarkcelebrations.co.uk
www.amberlarkcelebrations.co.uk

My logo can be found at the following Filevaultex location:
AI file: https://www.filevaultex.com/s/k4mprt8wn31b7hz/brandlogo_sourcefile.ai?dl=0
PNG file:
https://www.filevaultex.com/s/h9qsle2vbx07mnd/brandlogo_image.png?dl=0

Target Market(s)

women aged 30-55

Industry/Entity Type

Wedding

Contact Information for Business Card

in the following areas:

Moira Pennock
Event Planner
07715 482036

Font styles to use
Serif
Sans Serif
Script

Requirements
Must have
• Purple and white colour scheme
Should not have
• Black background
• Please don't submit any of the see-through business card designs.

```html
<!DOCTYPE html>
<html lang="en">
<head>
<meta charset="utf-8">
<title>Amber Lark Celebrations – Business Card</title>
<link rel="stylesheet" href="https://fonts.googleapis.com/css2?family=Open+Sans:wght@400;600;700&display=swap">
<style>
  :root {
    --backdrop: #3a302c;
    --card: #3a1748;
    --card-edge: #4a2259;
    --purple: #d59ae8;
    --purple-bright: #e2b3f1;
    --icon: #a54fc2;
    --white: #ffffff;
    --muted: #e6d6ec;
    --divider: #6a4479;
  }
  * { box-sizing: border-box; margin: 0; padding: 0; }
  html, body {
    width: 1200px; height: 844px; overflow: hidden;
    background: var(--backdrop);
    font-family: "Open Sans", Arial, sans-serif;
  }
  .stage {
    width: 1200px; height: 844px;
    display: flex; align-items: center; justify-content: center; gap: 40px;
  }
  .card {
    position: relative;
    width: 540px; height: 309px;
    background: var(--card);
    border: 1px solid var(--card-edge);
    border-radius: 3px;
    color: var(--white);
  }
  .brand {
    display: flex; align-items: center; gap: 12px;
    color: var(--purple);
    font-weight: 400;
    font-size: 26px;
    letter-spacing: 0.5px;
  }
  .brand-mark {
    width: 34px; height: 34px; border-radius: 50%;
    border: 2px solid var(--purple);
  }

  /* Front */
  .card-front .brand {
    position: absolute; top: 74px; left: 0; right: 0; justify-content: center;
  }
  .holder {
    position: absolute; left: 30px; top: 196px;
    width: 178px; text-align: right;
  }
  .holder-name {
    color: var(--purple-bright);
    font-weight: 600; font-size: 23px; line-height: 1.2;
  }
  .holder-role {
    color: var(--muted);
    font-weight: 400; font-size: 13px; letter-spacing: 0.6px;
    margin-top: 2px;
  }
  .contact-divider {
    position: absolute; left: 222px; top: 176px;
    width: 1px; height: 100px; background: var(--divider);
  }
  .contact-list {
    position: absolute; left: 240px; top: 182px;
    list-style: none;
  }
  .contact-list li {
    display: flex; align-items: center; gap: 9px;
    font-size: 14px; line-height: 1; margin-bottom: 11px;
    white-space: nowrap;
  }
  .contact-icon {
    width: 20px; height: 20px; border-radius: 3px;
    background: var(--icon);
    display: flex; align-items: center; justify-content: center;
    flex-shrink: 0;
  }

  /* Back */
  .card-back .brand {
    position: absolute; top: 70px; left: 0; right: 0; justify-content: center;
  }
  .services {
    position: absolute; top: 142px; left: 0; right: 0;
    text-align: center; font-size: 14.5px; line-height: 1.45;
  }
  .services strong { font-weight: 700; }
  .services .areas { margin-top: 22px; }
</style>
</head>
<body>
<main class="stage">

  <section class="card card-front" aria-label="Card front">
    <div class="brand"><span class="brand-mark"></span><span class="brand-name">Amber Lark Celebrations</span></div>
    <div class="holder">
      <p class="holder-name">Moira Pennock</p>
      <p class="holder-role">Event Planner</p>
    </div>
    <div class="contact-divider"></div>
    <ul class="contact-list">
      <li>
        <span class="contact-icon">
          <svg width="12" height="12" viewBox="0 0 12 12" aria-hidden="true"><path d="M2.5 1 L4.5 1 L5 3.5 L3.8 4.4 Q5 6.9 7.6 8.2 L8.5 7 L11 7.5 L11 9.5 Q10.5 11 9 11 Q1 10 1 2.5 Q1 1 2.5 1 Z" fill="#fff"/></svg>
        </span>07715 482036
      </li>
      <li>
        <span class="contact-icon">
          <svg width="12" height="10" viewBox="0 0 12 10" aria-hidden="true"><rect x="0.7" y="0.7" width="10.6" height="8.6" fill="none" stroke="#fff" stroke-width="1.3"/><path d="M0.7 0.9 L6 5.5 L11.3 0.9" fill="none" stroke="#fff" stroke-width="1.3"/></svg>
        </span>moira@amberlarkcelebrations.co.uk
      </li>
      <li>
        <span class="contact-icon">
          <svg width="12" height="12" viewBox="0 0 12 12" aria-hidden="true"><g fill="none" stroke="#fff" stroke-width="1.5" stroke-linecap="round"><path d="M5 7 L7 5"/><path d="M4.2 5.6 L2.6 7.2 A1.8 1.8 0 0 0 4.8 9.4 L6.4 7.8"/><path d="M7.8 6.4 L9.4 4.8 A1.8 1.8 0 0 0 7.2 2.6 L5.6 4.2"/></g></svg>
        </span>www.amberlarkcelebrations.co.uk
      </li>
    </ul>
  </section>

  <section class="card card-back" aria-label="Card back">
    <div class="brand"><span class="brand-mark"></span><span class="brand-name">Amber Lark Celebrations</span></div>
    <div class="services">
      <p><strong>Events:</strong> Weddings | Birthdays | Conferences |</p>
      <p>Product Launches | Fashion Shows</p>
      <p class="areas"><strong>Convention Areas:</strong> Wiltshire | Oxfordshire | Berkshire | London</p>
    </div>
  </section>

</main>
</body>
</html>
```